Bramblewick Gardening Services. A6 flyer single sided

Need an A6 flyer designing. Single sided.
I am a gardener.
I do lawn mowing - one-off garden tidy ups or regular fortnightly visits.
All kinds of trees expertly felled, topped or pruned.
Hedge cutting.
Fencing replaced or repaired.
Fully insured.
Access to fully qualified and licenced tree arborist
07724 316048 or 01632 742918.

I have attached my business card and letter head logo.
I'm open to new designs without incorporating any of my artwork.

Industry/Entity Type

Gardener

```html
<!DOCTYPE html>
<html lang="en">
<head>
<meta charset="utf-8">
<title>Bramblewick Garden Services – A6 Flyer</title>
<link rel="stylesheet" href="https://fonts.googleapis.com/css2?family=Questrial&family=Coustard:wght@900&display=swap">
<style>
  :root {
    --sky-top: #a9b2c6;
    --sky-bottom: #b8c0d2;
    --olive: #4b5a37;
    --ink: #1c1a17;
    --white: #ffffff;
    --leaf-light: #7fae3a;
    --leaf-mid: #4f8a24;
    --leaf-dark: #1f4a12;
  }
  html, body {
    margin: 0;
    padding: 0;
    width: 1200px;
    height: 859px;
    overflow: hidden;
  }
  .flyer {
    position: relative;
    width: 1200px;
    height: 859px;
    overflow: hidden;
    background: linear-gradient(180deg, var(--sky-top) 0%, var(--sky-bottom) 100%);
  }
  .service {
    position: absolute;
    margin: 0;
    line-height: 1;
    white-space: nowrap;
    font-family: "Questrial", sans-serif;
    font-weight: 400;
    color: var(--olive);
    text-shadow: 2px 3px 4px rgba(40, 50, 30, 0.35);
  }
  .service--hero { font-size: 98px; letter-spacing: -1px; }
  .service--major { font-size: 82px; letter-spacing: -1px; }
  .service--minor { font-size: 40px; }

  .gardening { left: 38px; top: 62px; }
  .regular-visits { left: 44px; top: 182px; font-size: 41px; }
  .lawn-mowing { left: 40px; top: 232px; }
  .tidy-ups { left: 620px; top: 50px; font-size: 43px; }
  .tree-work { left: 620px; top: 127px; font-size: 37px; }
  .hedge-cutting { left: 616px; top: 180px; }
  .fencing { left: 620px; top: 270px; font-size: 38px; }

  .credentials {
    position: absolute;
    left: 0;
    right: 0;
    text-align: center;
    margin: 0;
    font-family: "Coustard", serif;
    font-weight: 900;
    color: var(--ink);
    line-height: 1;
  }
  .insured { top: 350px; font-size: 27px; }
  .arborist { top: 391px; font-size: 26px; }
  .phones { top: 444px; font-size: 47px; letter-spacing: 1px; }

  .hedge {
    position: absolute;
    left: 0;
    top: 0;
    width: 1200px;
    height: 859px;
  }

  .business-name {
    position: absolute;
    left: 0;
    right: 0;
    top: 668px;
    margin: 0;
    text-align: center;
    font-family: "Coustard", serif;
    font-weight: 900;
    font-size: 80px;
    line-height: 92px;
    color: var(--white);
    text-shadow: 2px 3px 6px rgba(0, 0, 0, 0.45);
  }
</style>
</head>
<body>
  <main class="flyer">
    <svg class="hedge" viewBox="0 0 1200 859" role="img" aria-label="Photograph of a neatly clipped green laurel hedge with glossy leaves against the sky">
      <defs>
        <linearGradient id="hedgeFill" x1="0" y1="0" x2="0" y2="1">
          <stop offset="0" stop-color="var(--leaf-light)"/>
          <stop offset="0.45" stop-color="var(--leaf-mid)"/>
          <stop offset="1" stop-color="var(--leaf-dark)"/>
        </linearGradient>
      </defs>
      <path fill="url(#hedgeFill)" d="M0 490 C40 470 70 520 110 500 C150 480 170 540 220 520 C260 500 290 520 330 515 C370 505 380 470 420 485 C460 500 480 520 520 500 C560 480 580 520 620 505 C660 490 700 540 740 520 C770 505 780 470 820 490 C860 510 900 560 940 545 C980 530 1000 480 1040 500 C1080 520 1100 570 1140 555 C1170 545 1185 560 1200 560 L1200 859 L0 859 Z"/>
    </svg>

    <p class="service service--hero gardening">Gardening</p>
    <p class="service service--minor regular-visits">Regular fortnightly visits</p>
    <p class="service service--major lawn-mowing">Lawn Mowing</p>

    <p class="service service--minor tidy-ups">One-off garden tidy ups</p>
    <p class="service service--minor tree-work">Tree Felling, topping &amp; pruning</p>
    <p class="service service--major hedge-cutting">Hedge cutting</p>
    <p class="service service--minor fencing">Fencing - replaced/repaired</p>

    <p class="credentials insured">Fully insured</p>
    <p class="credentials arborist">Access to fully qualified and licenced tree arborist</p>
    <p class="credentials phones">07724 316048 or 01632 742918</p>

    <h1 class="business-name">Bramblewick<br>Garden Services</h1>
  </main>
</body>
</html>
```